依頼概要
◆概要・特徴
弊社はweb上で印刷を承る印刷通販を運営しております。
https://qorvaprint.example/
お客様が選んで使える「感染症対策ポスター」のデザイン作成をお願いいたします。

【当選内容】
複数当選(最大3点)を予定しておりますので、ご応募は1点ずつお願いいたします。
お一人様で何点でもご応募いただけます。

【デザインの要望】
・オフィス内、飲食内、旅館など様々な場所を想定しておりますので共通性・汎用性のあるデザインを宜しくお願いします。
イメージ画像を添付します。

【サイズ詳細】
作成サイズ A2トンボ付き

その他何かご不明な点がございましたら、お気軽にご質問下さい。
よろしくお願いいたします。
皆様、ご応募いただき誠にありがとうございます。
当選デザインについてはなるべくテイストが異なるものを選びたいと思っており、添付画像のような爽やかなカラフル感?も頂けると嬉しいです。
■ 選んだ理由

汎用性があるデザイン(オフィス内・飲食・etc)で清潔さがあるのをレギュラーとしながらも明るい感じのデザインも望んでおりました為、選ばせていただきました。

■ 提案者全員のお礼・コメント

大変よく出来たデザインばかりだったため、選ぶのに非常に悩んでおりました。
この度は貴重なデザインを応募頂き誠にありがとうございました。

```html
<!DOCTYPE html>
<html lang="ja">
<head>
<meta charset="UTF-8">
<title>感染防止対策ポスター</title>
<link href="https://fonts.googleapis.com/css2?family=Noto+Sans+JP:wght@400;500;700&display=swap" rel="stylesheet">
<style>
  :root {
    --paper: #ffffff;
    --leaf-tint: #dfeacf;
    --leaf-soft: #edf4e3;
    --badge: #8db66b;
    --badge-line: #8db66b;
    --icon: #ffffff;
    --title: #6f9350;
    --caption: #5d6f4d;
    --code: #4a4a4a;
  }
  * { margin: 0; padding: 0; box-sizing: border-box; }
  html, body { width: 879px; height: 1200px; overflow: hidden; background: var(--paper); }
  body { font-family: "Noto Sans JP", sans-serif; }
  .poster { position: relative; width: 879px; height: 1200px; background: var(--paper); overflow: hidden; }

  .leaf-wash { position: absolute; inset: 0; }
  .leaf-wash--top {
    background:
      radial-gradient(ellipse 300px 240px at 40px 40px, var(--leaf-tint), rgba(255,255,255,0) 75%),
      radial-gradient(ellipse 320px 260px at 860px 60px, var(--leaf-tint), rgba(255,255,255,0) 75%),
      radial-gradient(ellipse 220px 180px at 440px -40px, var(--leaf-soft), rgba(255,255,255,0) 75%),
      radial-gradient(ellipse 160px 260px at -20px 520px, var(--leaf-soft), rgba(255,255,255,0) 75%),
      radial-gradient(ellipse 160px 260px at 900px 560px, var(--leaf-soft), rgba(255,255,255,0) 75%);
  }
  .leaf-wash--bottom {
    background:
      radial-gradient(ellipse 360px 260px at 60px 1160px, var(--leaf-tint), rgba(255,255,255,0) 75%),
      radial-gradient(ellipse 360px 260px at 830px 1170px, var(--leaf-tint), rgba(255,255,255,0) 75%),
      radial-gradient(ellipse 420px 200px at 440px 1240px, var(--leaf-soft), rgba(255,255,255,0) 75%);
  }

  .headline { position: absolute; top: 100px; left: 0; right: 0; text-align: center; color: var(--title);
    font-weight: 500; font-size: 47px; line-height: 66px; letter-spacing: 2px; }

  .measures { position: absolute; top: 262px; left: 130px; width: 620px;
    display: grid; grid-template-columns: repeat(3, 206px); column-gap: 1px; row-gap: 26px; }
  .measure { display: flex; flex-direction: column; align-items: center; }
  .measure__badge { width: 206px; height: 206px; display: block; }
  .measure__text { margin-top: 16px; font-size: 14px; line-height: 22px; color: var(--caption); text-align: center; height: 44px; }

  .staff { position: absolute; top: 862px; left: 0; right: 0; text-align: center; }
  .staff__title { color: var(--title); font-size: 27px; font-weight: 500; letter-spacing: 1px; }
  .staff__detail { margin-top: 4px; color: var(--caption); font-size: 15px; letter-spacing: 1px; }
  .staff__icons { margin: 24px auto 0; width: 520px; display: flex; justify-content: space-between; }
  .staff__icon { width: 92px; height: 92px; display: block; }

  .print-code { position: absolute; left: 0; right: 0; bottom: 28px; text-align: center; font-size: 15px; color: var(--code); letter-spacing: 3px; }
</style>
</head>
<body>
<main class="poster">
  <div class="leaf-wash leaf-wash--top" role="img" aria-label="淡い緑の葉の背景"></div>
  <div class="leaf-wash leaf-wash--bottom" role="img" aria-label="淡い緑の葉の背景"></div>

  <h1 class="headline">新型コロナウィルス<br>感染防止対策を実施しています。</h1>

  <section class="measures">
    <div class="measure">
      <svg class="measure__badge" viewBox="0 0 206 206" role="img" aria-label="マスクのアイコン">
        <circle cx="103" cy="103" r="103" fill="var(--badge)"/>
        <path d="M56 92 Q40 92 40 108 Q40 126 62 128" fill="none" stroke="var(--icon)" stroke-width="5"/>
        <path d="M150 92 Q166 92 166 108 Q166 126 144 128" fill="none" stroke="var(--icon)" stroke-width="5"/>
        <path d="M58 86 Q103 70 148 86 L146 126 Q103 146 60 126 Z" fill="var(--icon)"/>
        <path d="M64 98 Q103 86 142 98 M64 110 Q103 100 142 110 M64 122 Q103 114 142 122" fill="none" stroke="var(--badge)" stroke-width="3"/>
      </svg>
      <p class="measure__text">マスク着用のご協力を<br>お願いいたします</p>
    </div>
    <div class="measure">
      <svg class="measure__badge" viewBox="0 0 206 206" role="img" aria-label="消毒液ボトルのアイコン">
        <circle cx="103" cy="103" r="103" fill="var(--badge)"/>
        <rect x="78" y="46" width="34" height="10" rx="3" fill="var(--icon)"/>
        <rect x="100" y="46" width="30" height="7" fill="var(--icon)"/>
        <rect x="89" y="56" width="12" height="14" fill="var(--icon)"/>
        <rect x="80" y="70" width="30" height="10" rx="3" fill="var(--icon)"/>
        <rect x="70" y="80" width="50" height="86" rx="8" fill="var(--icon)"/>
        <path d="M88 112 h14 v-12 h-14 z" fill="none"/>
        <rect x="89" y="104" width="12" height="38" fill="var(--badge)"/>
        <rect x="76" y="117" width="38" height="12" fill="var(--badge)"/>
        <g fill="var(--icon)">
          <circle cx="140" cy="46" r="3"/><circle cx="150" cy="40" r="3"/><circle cx="150" cy="54" r="3"/>
          <circle cx="160" cy="46" r="3"/><circle cx="162" cy="34" r="3"/><circle cx="162" cy="60" r="3"/>
        </g>
      </svg>
      <p class="measure__text">入店時は手指の消毒を<br>お願いいたします</p>
    </div>
    <div class="measure">
      <svg class="measure__badge" viewBox="0 0 206 206" role="img" aria-label="非接触体温計のアイコン">
        <circle cx="103" cy="103" r="103" fill="var(--badge)"/>
        <path d="M96 64 H150 Q160 64 160 74 V94 Q160 102 150 102 H132 L124 150 H104 L110 102 H96 Z" fill="var(--icon)"/>
        <rect x="118" y="74" width="28" height="14" rx="2" fill="var(--badge)"/>
        <path d="M84 70 Q76 83 84 96 M72 64 Q60 83 72 102 M60 58 Q44 83 60 108" fill="none" stroke="var(--icon)" stroke-width="4" stroke-linecap="round"/>
      </svg>
      <p class="measure__text">入店時に体温を<br>計らせていただきます</p>
    </div>
    <div class="measure">
      <svg class="measure__badge" viewBox="0 0 206 206" role="img" aria-label="距離を保つことを示す矢印のアイコン">
        <circle cx="103" cy="103" r="103" fill="var(--badge)"/>
        <rect x="48" y="70" width="8" height="66" rx="4" fill="var(--icon)"/>
        <rect x="150" y="70" width="8" height="66" rx="4" fill="var(--icon)"/>
        <line x1="72" y1="103" x2="134" y2="103" stroke="var(--icon)" stroke-width="5"/>
        <path d="M66 103 L80 93 V113 Z M140 103 L126 93 V113 Z" fill="var(--icon)"/>
      </svg>
      <p class="measure__text">一定の距離を保ち<br>密を避けてください</p>
    </div>
    <div class="measure">
      <svg class="measure__badge" viewBox="0 0 206 206" role="img" aria-label="開いた窓のアイコン">
        <circle cx="103" cy="103" r="103" fill="var(--badge)"/>
        <rect x="50" y="58" width="106" height="92" fill="none" stroke="var(--icon)" stroke-width="6"/>
        <rect x="58" y="66" width="48" height="76" fill="none" stroke="var(--icon)" stroke-width="4"/>
        <rect x="84" y="66" width="64" height="76" fill="none" stroke="var(--icon)" stroke-width="4"/>
        <line x1="50" y1="158" x2="156" y2="158" stroke="var(--icon)" stroke-width="4"/>
      </svg>
      <p class="measure__text">定期的に<br>換気を行っています</p>
    </div>
    <div class="measure">
      <svg class="measure__badge" viewBox="0 0 206 206" role="img" aria-label="消毒スプレーと布巾のアイコン">
        <circle cx="103" cy="103" r="103" fill="var(--badge)"/>
        <rect x="52" y="82" width="54" height="74" rx="4" fill="var(--icon)"/>
        <path d="M62 92 h34 M62 104 h34 M62 116 h34 M62 128 h34 M62 140 h34" stroke="var(--badge)" stroke-width="2"/>
        <path d="M126 58 H150 V66 L140 70 V80 H130 Z" fill="var(--icon)"/>
        <path d="M126 80 H146 Q156 96 156 112 V156 H116 V112 Q116 96 126 80 Z" fill="var(--icon)"/>
        <g fill="var(--icon)"><circle cx="110" cy="58" r="3"/><circle cx="100" cy="52" r="3"/><circle cx="100" cy="64" r="3"/><circle cx="90" cy="58" r="3"/></g>
      </svg>
      <p class="measure__text">こまめに消毒・清掃を<br>実施しています</p>
    </div>
  </section>

  <section class="staff">
    <h2 class="staff__title">スタッフの感染防止管理を毎日行っています。</h2>
    <p class="staff__detail">検温・こまめな手洗い・手指消毒・うがい・接触確認アプリ</p>
    <div class="staff__icons">
      <svg class="staff__icon" viewBox="0 0 92 92" role="img" aria-label="体温計のアイコン">
        <circle cx="46" cy="46" r="43" fill="var(--paper)" stroke="var(--badge-line)" stroke-width="3"/>
        <rect x="40" y="16" width="12" height="50" rx="6" transform="rotate(40 46 46)" fill="none" stroke="var(--badge-line)" stroke-width="3"/>
        <circle cx="30" cy="66" r="7" fill="var(--badge-line)"/>
      </svg>
      <svg class="staff__icon" viewBox="0 0 92 92" role="img" aria-label="手洗いの泡のアイコン">
        <circle cx="46" cy="46" r="43" fill="var(--paper)" stroke="var(--badge-line)" stroke-width="3"/>
        <g fill="none" stroke="var(--badge-line)" stroke-width="3">
          <circle cx="36" cy="50" r="12"/><circle cx="56" cy="40" r="9"/><circle cx="56" cy="62" r="6"/><circle cx="40" cy="26" r="5"/>
        </g>
      </svg>
      <svg class="staff__icon" viewBox="0 0 92 92" role="img" aria-label="うがい用コップのアイコン">
        <circle cx="46" cy="46" r="43" fill="var(--paper)" stroke="var(--badge-line)" stroke-width="3"/>
        <path d="M30 32 H62 L57 70 H35 Z" fill="none" stroke="var(--badge-line)" stroke-width="3"/>
        <path d="M33 46 H59" stroke="var(--badge-line)" stroke-width="3"/>
        <path d="M46 14 Q40 22 46 26 Q52 22 46 14 Z" fill="var(--badge-line)"/>
      </svg>
      <svg class="staff__icon" viewBox="0 0 92 92" role="img" aria-label="スマートフォンのアイコン">
        <circle cx="46" cy="46" r="43" fill="var(--paper)" stroke="var(--badge-line)" stroke-width="3"/>
        <rect x="31" y="18" width="30" height="56" rx="5" fill="none" stroke="var(--badge-line)" stroke-width="3"/>
        <rect x="36" y="26" width="20" height="36" fill="var(--leaf-tint)"/>
        <circle cx="46" cy="68" r="2.5" fill="var(--badge-line)"/>
      </svg>
    </div>
  </section>

  <p class="print-code">20200830B1</p>
</main>
</body>
</html>
```